I need a business card design for my new clinic (SPORTS MEDICINE OF KNEE). I am orthopedist, expert in sports surgery, especially knee surgery. I prefer, as colors, the colors of my logo (green, black and white). I already have my logo and should appear on my card. It's good to see my site to have ideas (www.drlucianovarela.com)
It needs contain:
my name: Dr. Luciano Varela
my registration: CRM 584-902
my specialty: Cirurgia do Joelho / Esporte
my address: Centro Executivo - Pinheiral Plaza
Av. Doutor Augusto Brandão Cunha, 2740 sala 0836
Jd. Ipanema - Ribeirão Preto - SP
my phone number: Tel (16) 8245-3908
my clinic phone: (16) 3670-4851
my e-mail: drlucianovarela@mailbox-exemplo.com
my site: www.drlucianovarela.com

Target Market(s)

futures patients

Industry/Entity Type

Clinic

Requirements
Nice to have
• letters not overfilled
straight lines, with few curves

```html
<!DOCTYPE html>
<html lang="pt-BR">
<head>
<meta charset="utf-8">
<title>Dr. Luciano Varela – Cartão de visita</title>
<link rel="stylesheet" href="https://fonts.googleapis.com/css2?family=Noto+Sans:wght@400&display=swap">
<style>
  :root {
    --card-black: #1e1a19;
    --brand-green: #43bb7b;
    --text-white: #ffffff;
    --text-dark: #1e1a19;
    --page-bg: #ffffff;
  }
  * { margin: 0; padding: 0; box-sizing: border-box; }
  html, body {
    width: 1200px;
    height: 776px;
    overflow: hidden;
    background: var(--page-bg);
  }
  body {
    font-family: "Noto Sans", Verdana, sans-serif;
  }
  .business-card {
    position: relative;
    width: 1200px;
    height: 776px;
    background: var(--card-black);
    border-radius: 36px;
    overflow: hidden;
    color: var(--text-white);
  }
  .brand-mark {
    position: absolute;
    left: 48px;
    top: 39px;
    width: 183px;
    height: 170px;
    background: var(--brand-green);
    border-radius: 14px;
  }
  .brand-name {
    position: absolute;
    left: 281px;
    top: 59px;
    font-size: 92px;
    line-height: 92px;
    letter-spacing: 6px;
    font-weight: 400;
    color: var(--text-white);
  }
  .divider-bars {
    position: absolute;
    left: 732px;
    top: 39px;
  }
  .doctor-info {
    position: absolute;
    left: 807px;
    top: 39px;
    font-size: 31px;
    line-height: 42.3px;
  }
  .address-block {
    position: absolute;
    left: 37px;
    top: 297px;
    font-size: 31px;
    line-height: 42px;
  }
  .phone-band {
    position: absolute;
    left: 0;
    top: 553px;
    width: 100%;
    height: 111px;
    background: var(--brand-green);
    color: var(--text-dark);
  }
  .phone-list {
    position: absolute;
    left: 37px;
    top: 11.5px;
    font-size: 31px;
    line-height: 43px;
    display: grid;
    grid-template-columns: 280px auto;
  }
  .phone-label { white-space: nowrap; }
  .phone-value { white-space: nowrap; }
</style>
</head>
<body>
  <main class="business-card">
    <div class="brand-mark" aria-hidden="true"></div>
    <div class="brand-name">VARELA</div>

    <svg class="divider-bars" width="36" height="174" viewBox="0 0 36 174" aria-hidden="true">
      <rect x="0" y="0" width="10" height="174" fill="var(--brand-green)"/>
      <rect x="25" y="0" width="10" height="174" fill="var(--brand-green)"/>
    </svg>

    <section class="doctor-info">
      <p class="doctor-name">Dr. Luciano Varela</p>
      <p class="doctor-registration">CRM 584-902</p>
      <p class="doctor-specialty">Cirurgia do Joelho</p>
      <p class="doctor-specialty">Esporte</p>
    </section>

    <address class="address-block" style="font-style: normal;">
      <p>Centro Executivo - Pinheiral Plaza</p>
      <p>Av. Doutor Augusto Brandão Cunha, 2740 sala 0836</p>
      <p>Jd. Ipanema - Ribeirão Preto - SP</p>
      <p>drlucianovarela@mailbox-exemplo.com</p>
      <p>www.drlucianovarela.com</p>
    </address>

    <section class="phone-band">
      <div class="phone-list">
        <span class="phone-label">Phone number</span>
        <span class="phone-value">: Tel (16) 8245-3908</span>
        <span class="phone-label">Clinic phone</span>
        <span class="phone-value">: (16) 3670-4851</span>
      </div>
    </section>
  </main>
</body>
</html>
```